Business cards for law firm with global theme

I'd like business cards with contact info for two offices. They should include the colors and font of the new logo design, which is a stylized globe with an "F" in it. The feel should be very modern and professional.

```html
<!DOCTYPE html>
<html lang="en">
<head>
<meta charset="utf-8">
<title>Vantorra Law – Business Cards</title>
<link rel="stylesheet" href="https://fonts.googleapis.com/css2?family=Montserrat:wght@400;500;600;700&display=swap">
<style>
  :root {
    --stage: #e9e9e9;
    --navy: #063d72;
    --navy-deep: #04305c;
    --pattern-light: #1d63b0;
    --sky: #1aa3e6;
    --white: #ffffff;
    --edge: #22b0ef;
  }
  * { box-sizing: border-box; margin: 0; padding: 0; }
  html, body {
    width: 1200px; height: 802px; overflow: hidden;
    background: var(--stage);
    font-family: "Montserrat", sans-serif;
  }
  .stage {
    position: relative; width: 1200px; height: 802px;
    display: flex; align-items: center; justify-content: center; gap: 40px;
  }
  .card {
    position: relative; width: 540px; height: 309px;
    background: var(--navy);
    border-bottom: 3px solid var(--edge);
    box-shadow: 0 10px 24px rgba(0,0,0,.18);
    overflow: hidden;
    color: var(--white);
  }

  /* Front */
  .front .brand {
    position: absolute; left: 60px; top: 70px;
    display: flex; align-items: center; gap: 18px;
  }
  .brand-dot {
    width: 70px; height: 70px; border-radius: 50%;
    background: var(--sky);
  }
  .brand-name {
    font-weight: 700; font-size: 34px; letter-spacing: .5px;
    color: var(--white);
  }
  .brand-rule {
    position: absolute; left: 148px; top: 128px;
    width: 225px; height: 1px; background: var(--sky);
  }
  .person {
    position: absolute; left: 70px; top: 170px; text-align: right; width: 165px;
  }
  .person-name { color: var(--sky); font-weight: 500; font-size: 17px; letter-spacing: .8px; }
  .person-role { font-size: 13px; margin-top: 4px; }
  .divider {
    position: absolute; left: 252px; top: 165px; width: 1px; height: 62px;
    background: rgba(255,255,255,.7);
  }
  .contacts {
    position: absolute; left: 270px; top: 165px; list-style: none;
    font-size: 13px; line-height: 21px;
  }
  .contacts li { display: flex; align-items: center; gap: 8px; }
  .contacts svg { width: 11px; height: 11px; fill: var(--sky); flex: none; }
  .address {
    position: absolute; left: 120px; top: 252px; width: 380px; text-align: right;
    font-size: 13px;
  }

  /* Back */
  .back .pattern {
    position: absolute; inset: 0;
    background: linear-gradient(100deg, var(--navy-deep) 0%, var(--navy) 45%, var(--pattern-light) 100%);
  }
  .back .brand {
    position: absolute; right: 60px; top: 132px;
    display: flex; align-items: center; gap: 12px;
  }
  .back .brand-dot { width: 52px; height: 52px; background: var(--sky); }
  .back .brand-name { font-size: 24px; }
</style>
</head>
<body>
<main class="stage">
  <section class="card front" aria-label="Business card front">
    <div class="brand">
      <span class="brand-dot"></span>
      <span class="brand-name">VANTORRA LAW</span>
    </div>
    <span class="brand-rule"></span>

    <div class="person">
      <p class="person-name">DANIEL REYES</p>
      <p class="person-role">Manager</p>
    </div>
    <span class="divider"></span>
    <ul class="contacts">
      <li><svg viewBox="0 0 12 12"><path d="M2 1h3l1 3-2 1a7 7 0 0 0 3 3l1-2 3 1v3c-6 1-10-3-9-9z"/></svg>555-014-2100</li>
      <li><svg viewBox="0 0 12 12"><path d="M0 2h12v8H0z M0 2l6 5 6-5" /></svg>hello@vantorralaw.com</li>
      <li><svg viewBox="0 0 12 12"><circle cx="6" cy="6" r="6"/></svg>www.vantorralaw.com</li>
    </ul>
    <p class="address">Your Address, City, State, Zip 0000</p>
  </section>

  <section class="card back" aria-label="Business card back">
    <div class="pattern" role="img" aria-label="Repeating embossed brand-symbol pattern in deep and bright blues"></div>
    <div class="brand">
      <span class="brand-dot"></span>
      <span class="brand-name">VANTORRA LAW</span>
    </div>
  </section>
</main>
</body>
</html>
```